Harbor Zentrik needs a new Website Design

We need a WEB site landing page (/template) design, we currently have a company logo.We like the Valtor.com web designEnclosed is our company logo.Our Current website is https://www.harborzentrik.com.au/

1 page

```html
<!DOCTYPE html>
<html lang="en">
<head>
<meta charset="utf-8">
<title>Harbor Zentrik — White-Label Communications</title>
<link rel="stylesheet" href="https://fonts.googleapis.com/css2?family=Raleway:wght@400;500;600;700&family=Open+Sans:wght@400;600;700&display=swap">
<style>
:root{
  --indigo:#2f2a8c;
  --violet:#6b2fa3;
  --magenta:#8a2fa6;
  --blue:#1e9fe4;
  --white:#ffffff;
  --ink:#2d2d3a;
  --muted:#7a7a88;
  --light:#f2f2f4;
  --dark:#1d1f2b;
  --footer:#181a2e;
}
*{box-sizing:border-box;margin:0;padding:0}
html,body{width:1200px;height:3328px;overflow:hidden}
body{font-family:"Open Sans",Arial,sans-serif;color:var(--ink);background:var(--white);position:relative}
.section{position:absolute;left:0;width:1200px;overflow:hidden}
.abs{position:absolute}
.btn{position:absolute;display:inline-block;background:var(--blue);color:var(--white);font:700 11px/1 "Open Sans",Arial,sans-serif;letter-spacing:1px;text-transform:uppercase;border-radius:18px;padding:12px 22px;text-align:center}
.brand{position:absolute;font:700 26px/1 "Raleway",Arial,sans-serif;color:var(--white);display:flex;align-items:center;gap:10px}
.brand-dot{width:14px;height:14px;border-radius:50%;background:var(--blue)}

/* hero */
.hero{top:0;height:660px;background:linear-gradient(110deg,#2b2a8a 0%,#4b2c9c 45%,#7a2fa8 100%)}
.nav{position:absolute;top:64px;left:448px;display:flex;gap:22px;font:600 14px/1 "Open Sans",Arial,sans-serif;color:var(--white)}
.hero .btn.signup{top:56px;left:952px;padding:11px 20px}
.play{position:absolute;left:220px;top:258px;width:44px;height:44px;border-radius:50%;background:rgba(255,255,255,.25)}
.hero-title{position:absolute;left:220px;top:326px;width:520px;font:700 30px/1.3 "Raleway",Arial,sans-serif;color:var(--white)}
.hero-sub{position:absolute;left:220px;top:404px;font:400 13px/1 "Open Sans",Arial,sans-serif;color:rgba(255,255,255,.85)}
.hero .btn.how{top:490px;left:220px}

/* how it works */
.how{top:660px;height:650px;background:var(--white)}
.sec-title{position:absolute;left:0;width:1200px;text-align:center;font:500 30px/1 "Raleway",Arial,sans-serif}
.sec-sub{position:absolute;left:0;width:1200px;text-align:center;font:600 15px/1.4 "Raleway",Arial,sans-serif;color:var(--muted)}
.step{position:absolute;top:228px;width:240px;height:360px;background:var(--white);box-shadow:0 8px 30px rgba(40,30,90,.12)}
.step-art{position:absolute;left:60px;top:36px;width:120px;height:120px;border-radius:50%;background:linear-gradient(135deg,#e7e9f3,#cfd6ea)}
.step-text{position:absolute;left:20px;top:190px;width:200px;text-align:center;font:400 13px/1.5 "Open Sans",Arial,sans-serif;color:var(--muted)}
.step-mark{position:absolute;width:14px;height:3px;background:var(--violet);transform:rotate(-45deg)}
.dots{position:absolute;left:0;width:1200px;display:flex;justify-content:center;gap:14px}
.dots span{width:14px;height:14px;border-radius:50%;background:var(--magenta)}

/* services */
.services{top:1310px;height:570px;background:linear-gradient(115deg,#3b2a8e 0%,#5d2d9c 50%,#7a2fa3 100%)}
.services .sec-title{color:var(--white);top:108px;font-weight:400}
.service{position:absolute;width:240px;text-align:center;color:var(--white)}
.service-icon{width:18px;height:18px;margin:0 auto 12px;border-radius:4px;background:rgba(255,255,255,.9)}
.service h3{font:700 13px/1 "Open Sans",Arial,sans-serif;letter-spacing:1.5px;text-transform:uppercase;margin-bottom:14px}
.service p{font:400 12px/1.55 "Open Sans",Arial,sans-serif;color:rgba(255,255,255,.6)}

/* about */
.about{top:1880px;height:440px;background:linear-gradient(90deg,#1f2e24 0%,#2c3a2e 35%,#34363a 60%,#26272c 100%)}
.about-photo{position:absolute;inset:0}
.about-card{position:absolute;left:220px;top:40px;width:332px;height:400px;background:var(--white);box-shadow:0 10px 30px rgba(0,0,0,.3);text-align:center}
.about-card .brand{position:static;justify-content:center;color:var(--indigo);margin-top:120px}
.about-card p{font:400 14px/1.5 "Open Sans",Arial,sans-serif;color:var(--muted);margin:28px 40px 0}
.about-card .btn{left:106px;top:280px}
.about-head{position:absolute;left:640px;top:240px;width:420px;font:600 22px/1.4 "Raleway",Arial,sans-serif;color:var(--white)}

/* testimonials */
.testimonials{top:2320px;height:480px;background:var(--white)}
.quote{position:absolute;left:360px;top:176px;width:480px;text-align:center;font:400 14px/1.6 "Open Sans",Arial,sans-serif;color:var(--muted)}
.author{position:absolute;left:0;top:282px;width:1200px;text-align:center;font:700 12px/1 "Open Sans",Arial,sans-serif;letter-spacing:1.5px;color:var(--ink)}
.author-role{position:absolute;left:0;top:302px;width:1200px;text-align:center;font:400 11px/1 "Open Sans",Arial,sans-serif;color:var(--muted)}
.t-dots{position:absolute;left:0;top:358px;width:1200px;display:flex;justify-content:center;gap:10px}
.t-dots span{width:8px;height:8px;border-radius:50%;background:#cfcfd6}
.t-dots span.on{background:var(--muted)}

/* contact */
.contact{top:2800px;height:150px;background:var(--light)}
.company{position:absolute;left:64px;top:26px;font:400 16px/1.6 "Open Sans",Arial,sans-serif;color:var(--ink)}
.divider{position:absolute;left:352px;top:26px;width:1px;height:96px;background:#c9c9d0}
.col{position:absolute;top:30px;width:240px;text-align:center}
.col h4{font:600 18px/1 "Raleway",Arial,sans-serif;margin-bottom:14px}
.col p{font:400 13px/1.7 "Open Sans",Arial,sans-serif;color:var(--muted)}

/* support */
.support{top:2950px;height:250px;background:linear-gradient(100deg,#14161f 0%,#2a2d38 55%,#1a1c25 100%)}
.support-text{position:absolute;left:300px;top:62px;width:600px;text-align:center;font:600 16px/1.6 "Open Sans",Arial,sans-serif;color:var(--white)}
.support .btn{left:503px;top:150px}

/* footer */
.footer{top:3200px;height:128px;background:var(--footer)}
.footer .brand{left:180px;top:50px}
.footer .nav{top:58px;left:604px;font-size:14px}
</style>
</head>
<body>

<header class="section hero">
  <svg class="abs" style="left:0;top:0" width="1200" height="660" aria-hidden="true">
    <path d="M600 660 C 760 420 980 300 1200 280 L1200 660 Z" fill="rgba(160,60,190,.35)"/>
    <path d="M380 660 C 620 460 900 380 1200 420 L1200 660 Z" fill="rgba(120,40,170,.35)"/>
    <path d="M820 0 C 900 160 1060 220 1200 200 L1200 0 Z" fill="rgba(70,40,160,.35)"/>
    <path d="M0 520 C 200 470 420 520 560 660 L0 660 Z" fill="rgba(40,40,130,.35)"/>
    <path d="M700 0 C 760 260 1000 380 1200 360" stroke="rgba(255,255,255,.12)" stroke-width="2" fill="none"/>
  </svg>
  <div class="brand" style="left:128px;top:70px"><span class="brand-dot"></span>Harbor Zentrik</div>
  <nav class="nav"><span>Home</span><span>Voice</span><span>Data</span><span>Hardware</span><span>Services</span><span>Terms</span><span>Status</span></nav>
  <span class="btn signup">Sign Up</span>
  <div class="play"><svg width="44" height="44" aria-hidden="true"><path d="M18 14 L30 22 L18 30 Z" fill="#fff"/></svg></div>
  <h1 class="hero-title">White-Label Solution for All your Communication Needs</h1>
  <p class="hero-sub">Liberating Businesses From Traditional Communications Systems</p>
  <span class="btn how">How it works</span>
</header>

<section class="section how">
  <h2 class="sec-title" style="top:128px">How its works</h2>
  <p class="sec-sub" style="top:170px">We have all the components to start and<br>run your own White Label Telco</p>
  <div class="step" style="left:184px">
    <div class="step-art" role="img" aria-label="Line illustration of a cloud with network branches"></div>
    <p class="step-text">Send in your job, submit your job via email</p>
    <span class="step-mark" style="left:14px;top:334px"></span><span class="step-mark" style="left:212px;top:14px"></span>
  </div>
  <div class="step" style="left:480px">
    <div class="step-art" role="img" aria-label="Line illustration of a laptop with a video call"></div>
    <p class="step-text">We work on stage. Our expert team does the rest.</p>
    <span class="step-mark" style="left:14px;top:334px"></span><span class="step-mark" style="left:212px;top:14px"></span>
  </div>
  <div class="step" style="left:776px">
    <div class="step-art" role="img" aria-label="Line illustration of a hand holding a payment card"></div>
    <p class="step-text">Pay your first fee and let We it run!</p>
    <span class="step-mark" style="left:14px;top:334px"></span><span class="step-mark" style="left:212px;top:14px"></span>
  </div>
  <div class="dots" style="top:582px"><span></span><span></span><span></span></div>
</section>

<section class="section services">
  <svg class="abs" style="left:0;top:0" width="1200" height="570" aria-hidden="true">
    <path d="M0 0 C 200 120 320 360 260 570 L0 570 Z" fill="rgba(40,30,120,.35)"/>
    <path d="M1200 0 C 1000 140 920 380 1000 570 L1200 570 Z" fill="rgba(150,50,170,.3)"/>
    <path d="M300 0 C 500 200 760 240 1200 120" stroke="rgba(255,255,255,.08)" stroke-width="2" fill="none"/>
  </svg>
  <h2 class="sec-title">Our Services</h2>
  <div class="service" style="left:188px;top:216px"><div class="service-icon"></div><h3>Cloud IP PBX</h3><p>Hosted phone system with full call routing, queues and voicemail for teams.</p></div>
  <div class="service" style="left:480px;top:216px"><div class="service-icon"></div><h3>Unified Communications</h3><p>Voice, chat, video and presence joined in one simple app for staff.</p></div>
  <div class="service" style="left:776px;top:216px"><div class="service-icon"></div><h3>Invoice &amp; Payment Platform</h3><p>Bill your own customers with branded invoices and automated payments.</p></div>
  <div class="service" style="left:336px;top:432px"><div class="service-icon"></div><h3>Data Services</h3><p>Fast business broadband and private links with local support included.</p></div>
  <div class="service" style="left:628px;top:432px"><div class="service-icon"></div><h3>Voice Services</h3><p>Business grade SIP trunks and numbers with clear, reliable calling.</p></div>
</section>

<section class="section about">
  <div class="about-photo" role="img" aria-label="Photo of a plant beside a laptop on a desk"></div>
  <div class="about-card">
    <div class="brand"><span class="brand-dot"></span>Harbor Zentrik</div>
    <p>White-Label Solution for All your Communication Needs</p>
    <span class="btn">More about us</span>
  </div>
  <h2 class="about-head">Australia's Business Grade Unified Communications Company</h2>
</section>

<section class="section testimonials">
  <h2 class="sec-title" style="top:112px;font-weight:400">Testimonials</h2>
  <p class="quote">I have been enormously thankful for your support in the design of my website. You have been a skilful and patient teacher and advisor.</p>
  <p class="author">MARLOW FENWICK</p>
  <p class="author-role">Customer</p>
  <div class="t-dots"><span class="on"></span><span></span><span></span><span></span></div>
</section>

<section class="section contact">
  <p class="company">ABN 48 900 215 377<br>PO Box 4410 Eastbrook<br>ACT 2900</p>
  <span class="divider"></span>
  <div class="col" style="left:488px"><h4>Administration</h4><p>admin@harborzentrik.com.au<br>+61 2 5550 0142</p></div>
  <div class="col" style="left:700px"><h4>Accounts</h4><p>admin@harborzentrik.com.au<br>+61 2 5550 0142</p></div>
  <div class="col" style="left:930px"><h4>Support</h4><p>admin@harborzentrik.com.au<br>+61 2 5550 0142</p></div>
</section>

<section class="section support">
  <div class="abs" style="inset:0" role="img" aria-label="Dark photo of a desk with a keyboard and mouse"></div>
  <p class="support-text">Our technical support team is always available to you via phone, live chat and support ticketing system.</p>
  <span class="btn">Take a support</span>
</section>

<footer class="section footer">
  <div class="brand"><span class="brand-dot"></span>Harbor Zentrik</div>
  <nav class="nav"><span>Home</span><span>Voice</span><span>Data</span><span>Hardware</span><span>Services</span><span>Terms</span><span>Status</span></nav>
</footer>

</body>
</html>
```